business cards, stationeries, templates(proposals, company profile, presentations, folders, cd..etc)
PXD Harbor Lumen Works
Professional
Tamer Fouad
Founder - Sr. Team Lead
Harbor Lumen Works LLC. Business & Technology Services Level 14 Falcon Crest Tower, Palm Avenue P.O. Box 57312, Jeddah 23816 Kingdom of Saudi Arabia
tamer@hlworks.example
www.hlworks.example
Please consider that the business cards will include multi language information (english & Arabic) probably on the same side of business card, more over we need to have a small barcode thats going to include business card information along with company social media links. ------------- twitter account: pxdchirps https://twitter.example/pxdchirps youtube: pxdreel http://www.videohub.example/user/pxdreel Vimeo: pxdm http://clipsite.example/pxdm Facebook: hlworks.example https://www.friendbook.example/hlworks.example
open for creative suggestions,,,

```html
<!DOCTYPE html>
<html lang="en">
<head>
<meta charset="utf-8">
<title>Harbor Lumen Works – Business Card</title>
<link rel="stylesheet" href="https://fonts.googleapis.com/css2?family=Michroma&display=swap">
<style>
  :root {
    --backdrop: #e4e5e7;
    --card: #ffffff;
    --brand-blue: #2a8fd8;
    --brand-grey: #77787b;
    --text-dark: #4a4b4d;
  }
  * { margin: 0; padding: 0; box-sizing: border-box; }
  html, body {
    width: 1200px; height: 895px; overflow: hidden;
    background: var(--backdrop);
    font-family: "Michroma", sans-serif;
  }
  .stage { position: relative; width: 1200px; height: 895px; }
  .card {
    position: absolute; top: 290px;
    width: 540px; height: 310px;
    background: var(--card);
    box-shadow: 0 2px 10px rgba(0,0,0,0.12);
    overflow: hidden;
  }
  .card--front { left: 40px; }
  .card--back { left: 620px; }

  .brand {
    position: absolute; display: flex; align-items: center; gap: 10px;
    color: var(--brand-blue); white-space: nowrap;
  }
  .brand__square { flex: none; width: 12px; height: 12px; background: var(--brand-blue); }
  .brand__name { font-size: 15px; letter-spacing: 0.5px; line-height: 1; }
  .card--front .brand { left: 130px; top: 48px; }
  .card--back .brand { left: 50%; top: 50%; transform: translate(-50%, -50%); }
  .card--back .brand__square { width: 16px; height: 16px; }
  .card--back .brand__name { font-size: 20px; }

  .person { position: absolute; left: 130px; top: 112px; }
  .person__name { font-size: 15px; color: var(--brand-blue); letter-spacing: 1px; text-transform: uppercase; }
  .person__role { font-size: 8px; color: var(--brand-grey); letter-spacing: 1px; text-transform: uppercase; margin-top: 6px; }

  .address {
    position: absolute; left: 44px; top: 168px;
    display: flex; gap: 10px; align-items: flex-start;
    font-size: 9px; color: var(--text-dark); line-height: 1.7;
  }
  .address svg { flex: none; margin-top: 2px; }

  .web-rule { position: absolute; left: 44px; top: 214px; width: 250px; height: 5px; background: var(--brand-blue); }
  .web { position: absolute; left: 44px; top: 228px; font-size: 9px; color: var(--text-dark); }

  .contacts {
    position: absolute; left: 330px; top: 176px;
    list-style: none; font-size: 9px; color: var(--text-dark);
  }
  .contacts li { display: flex; align-items: center; gap: 10px; height: 19px; }
  .contacts svg { flex: none; }

  .footer-band { position: absolute; left: 0; bottom: 22px; height: 7px; width: 100%; display: flex; }
  .footer-band__blue { width: 58%; background: var(--brand-blue); }
  .footer-band__grey { flex: 1; background: var(--brand-grey); margin-left: 6px; }
</style>
</head>
<body>
<main class="stage">

  <section class="card card--front" aria-label="Business card front">
    <div class="brand">
      <span class="brand__square"></span>
      <span class="brand__name">PXD Harbor Lumen Works</span>
    </div>

    <div class="person">
      <p class="person__name">Omar Halden</p>
      <p class="person__role">General Manager</p>
    </div>

    <div class="address">
      <svg width="9" height="12" viewBox="0 0 9 12" aria-hidden="true">
        <path d="M4.5 0C2 0 0 2 0 4.5 0 8 4.5 12 4.5 12S9 8 9 4.5C9 2 7 0 4.5 0z" fill="var(--brand-blue)"/>
        <circle cx="4.5" cy="4.5" r="1.6" fill="#fff"/>
      </svg>
      <p>27 Harbor Lane,<br>Palm Avenue JED</p>
    </div>

    <div class="web-rule"></div>
    <p class="web">www.hlworks.example</p>

    <ul class="contacts">
      <li>
        <svg width="9" height="11" viewBox="0 0 9 11" aria-hidden="true"><rect x="0.5" y="0.5" width="8" height="10" rx="1.5" fill="none" stroke="var(--brand-grey)"/><rect x="2" y="2" width="5" height="5" fill="var(--brand-grey)"/></svg>
        <span>012 555 0142</span>
      </li>
      <li>
        <svg width="10" height="10" viewBox="0 0 10 10" aria-hidden="true"><path d="M2 0.5l2 2.3-1 1.2c.6 1.3 1.6 2.3 2.9 2.9l1.2-1 2.3 2L8.6 9.6C4.4 9.6.4 5.6.4 1.4z" fill="var(--brand-grey)"/></svg>
        <span>012 555 0142</span>
      </li>
      <li>
        <svg width="11" height="8" viewBox="0 0 11 8" aria-hidden="true"><rect x="0.5" y="0.5" width="10" height="7" fill="none" stroke="var(--brand-grey)"/><path d="M0.5 0.5l5 4 5-4" fill="none" stroke="var(--brand-grey)"/></svg>
        <span>omar@hlworks.example</span>
      </li>
    </ul>

    <div class="footer-band">
      <div class="footer-band__blue"></div>
      <div class="footer-band__grey"></div>
    </div>
  </section>

  <section class="card card--back" aria-label="Business card back">
    <div class="brand">
      <span class="brand__square"></span>
      <span class="brand__name">PXD Harbor Lumen Works</span>
    </div>
  </section>

</main>
</body>
</html>
```